Wordpress site needed asap for modern mobile app dev company

Hi
We are looking for someone to design a very modern looking website with company logo that outlines what our business is and let's users purchase a mobile app designed by our company. (For ideas think zentrobo.io or quillforge.com) The user should be able to describe what functionality they require and we will go and provide a test version of their app built .
The pages we would like are:
Home
Pricing (giving them an option to buy the options available)
Testimonials
Contact
I currently have hosting on KVD Hosting with wordpress installed, so if this could be taken into account that would be great. I also have marble drift template if this could be incorporated.

```html
<!DOCTYPE html>
<html lang="en">
<head>
<meta charset="utf-8">
<title>Ventra — Mobile App Developer</title>
<link href="https://fonts.googleapis.com/css2?family=Roboto:wght@300;400;500;700&family=Open+Sans:ital,wght@0,400;0,600;1,400&display=swap" rel="stylesheet">
<style>
:root{
  --blue:#27a3dd;
  --blue-dark:#1b8cc4;
  --orange:#f39a1c;
  --orange-dark:#e08600;
  --ink:#333;
  --muted:#888;
  --white:#fff;
  --light:#f3f3f3;
  --line:#e4e4e4;
}
*{box-sizing:border-box;margin:0;padding:0}
html,body{width:1200px;height:3403px;overflow:hidden}
body{position:relative;font-family:"Open Sans",Arial,sans-serif;color:var(--ink);background:var(--white)}
.abs{position:absolute}
.heading{font-family:"Roboto",Arial,sans-serif}

/* header */
.site-header{left:0;top:0;width:1200px;height:102px;background:var(--white);border-top:4px solid var(--blue)}
.brand{left:100px;top:30px;display:flex;align-items:center;gap:12px;font-family:"Roboto",sans-serif;font-weight:700;font-size:30px;color:var(--blue)}
.brand-mark{width:40px;height:40px;background:var(--orange);border-radius:3px}
.nav{left:406px;top:0;height:98px;display:flex;font-family:"Roboto",sans-serif;font-size:11.5px;font-weight:500;text-transform:uppercase;color:#444;white-space:nowrap}
.nav a{display:flex;align-items:center;padding:0 14px;color:inherit;text-decoration:none}
.nav a.active{background:var(--blue);color:var(--white);padding:0 22px}
.btn{display:flex;align-items:center;justify-content:center;font-family:"Roboto",sans-serif;font-weight:500;font-size:12px;text-transform:uppercase;color:var(--white);border-radius:3px;white-space:nowrap}
.btn-orange{background:var(--orange);border-bottom:3px solid var(--orange-dark)}
.btn-blue{background:var(--blue);border-bottom:3px solid var(--blue-dark)}
.signup{left:1005px;top:30px;width:96px;height:36px;gap:6px}

/* hero */
.hero{left:0;top:102px;width:1200px;height:495px;background:linear-gradient(100deg,#1c2630 0%,#27394a 45%,#31516a 70%,#1d2a38 100%)}
.hero-title{left:100px;top:205px;font-size:40px;font-weight:700;color:var(--white);letter-spacing:.5px}
.hero-sub{left:100px;top:258px;font-size:32px;font-weight:300;color:var(--white)}
.email-input{left:100px;top:342px;width:336px;height:40px;background:#eee;font-size:12px;color:#777;padding:12px 18px}
.email-btn{left:436px;top:342px;width:126px;height:40px;border-radius:0}
.store-badge{top:424px;width:167px;height:53px;border:2px solid rgba(255,255,255,.8);border-radius:4px;background:rgba(0,0,0,.35)}
.hero-arrow{top:335px;width:28px;height:28px;border-radius:50%;background:rgba(255,255,255,.85);display:flex;align-items:center;justify-content:center}

/* about */
.about-photo{left:0;top:597px;width:556px;height:430px;background:linear-gradient(135deg,#cfd6dc 0%,#e9ecef 45%,#8e9aa3 100%)}
.section-title{font-family:"Roboto",sans-serif;font-size:28px;font-weight:500;color:var(--blue);text-transform:uppercase}
.about-text{left:606px;width:500px;font-size:12.5px;line-height:23px;color:#777}

/* offer */
.center-title{left:0;width:1200px;text-align:center}
.center-sub{left:170px;width:860px;text-align:center;font-size:13px;line-height:25px;color:#888}
.phones{left:100px;top:1202px;width:358px;height:488px;background:linear-gradient(160deg,#2b2b2b 0%,#1e6fa8 50%,#111 100%);border-radius:30px}
.feature-icon{left:601px;width:91px;height:91px;border-radius:50%;display:flex;align-items:center;justify-content:center;border:5px solid #eee}
.feature-title{left:714px;font-family:"Roboto",sans-serif;font-size:15px;font-weight:500;text-transform:uppercase}
.feature-text{left:714px;width:390px;font-size:12px;line-height:24px;color:#888}
.feature-rule{left:714px;width:390px;height:1px;background:var(--line)}
.timeline{left:646px;top:1295px;width:1px;height:180px;border-left:2px dotted #ccc}

/* pricing */
.pricing{left:0;top:1749px;width:1200px;height:621px;background:linear-gradient(120deg,#22241f 0%,#3b3526 40%,#1a1e20 70%,#2d3a44 100%)}
.price-card{background:var(--white);text-align:center;border-top:5px solid var(--blue)}
.price-card.featured{border-top-color:var(--orange);box-shadow:0 0 18px rgba(0,0,0,.4)}
.plan{font-family:"Roboto",sans-serif;font-size:15px;font-weight:500;margin-top:28px;color:var(--blue)}
.amount{font-family:"Roboto",sans-serif;font-size:26px;color:var(--blue);margin-top:10px}
.featured .plan,.featured .amount{color:var(--orange)}
.per{font-size:10px;color:#999;margin-top:8px;text-transform:uppercase}
.plan-list{list-style:none;margin-top:24px;font-size:10px;color:#666;text-transform:uppercase}
.plan-list li{height:34px;line-height:34px;border-top:1px solid var(--line)}
.plan-list li:nth-child(odd){background:#f6f6f6}
.card-btn{width:130px;height:40px;margin:18px auto 0;gap:8px}

/* testimonials */
.testimonials{left:0;top:2370px;width:1200px;height:454px;background:var(--light)}
.quote-disc{left:492px;top:2498px;width:100px;height:100px;border-radius:50%;background:var(--white);display:flex;align-items:center;justify-content:center;font-family:Georgia,serif;font-size:90px;color:var(--blue);line-height:1;padding-top:40px}
.avatar{left:578px;top:2488px;width:130px;height:130px;border-radius:50%;background:radial-gradient(circle at 50% 40%,#d8c0ac,#8c7566);border:5px solid var(--white)}
.quote-text{left:150px;top:2646px;width:900px;text-align:center;font-style:italic;font-size:12px;line-height:28px;color:#888}
.quote-mark{font-family:Georgia,serif;font-size:50px;color:#ccc}
.author{left:0;top:2740px;width:1200px;text-align:center;font-size:12px;color:#888}
.author b{color:var(--orange);font-weight:600}

/* contact */
.contact{left:0;top:2824px;width:1200px;height:478px;background:linear-gradient(90deg,#2a2419 0%,#3d3424 45%,#7a6a4a 70%,#b49a6e 100%)}
.field{background:#f3f3f3;border:5px solid rgba(255,255,255,.35);background-clip:padding-box;font-size:12px;color:#888;padding:11px 14px}

/* footer */
.site-footer{left:0;top:3302px;width:1200px;height:101px;background:var(--blue);color:var(--white)}
.foot-links{left:100px;top:3332px;font-family:"Roboto",sans-serif;font-size:11px;font-weight:500;text-transform:uppercase;white-space:nowrap}
.foot-copy{left:100px;top:3356px;font-size:10px;text-transform:uppercase;white-space:nowrap}
.social{width:40px;height:40px;border-radius:50%;border:2px solid var(--white)}
</style>
</head>
<body>

<header class="abs site-header">
  <div class="abs brand"><span class="brand-mark"></span>VENTRA</div>
  <nav class="abs nav">
    <a class="active">Home</a><a>Who we are</a><a>What we offer</a><a>Pricing</a><a>Testimonials</a><a>Contact</a>
  </nav>
  <div class="abs btn btn-orange signup">Sign up</div>
</header>

<section class="abs hero" role="img" aria-label="Businessman holding a smartphone with floating app icons"></section>
<h1 class="abs heading hero-title">MOBILE APP DEVELOPER</h1>
<p class="abs hero-sub">for small business &amp; enterprises.</p>
<div class="abs email-input">Enter Your e-mail Address...</div>
<div class="abs btn btn-orange email-btn">Subscribe</div>
<div class="abs store-badge" style="left:100px"></div>
<div class="abs store-badge" style="left:281px"></div>
<div class="abs hero-arrow" style="left:36px"><svg width="10" height="12"><path d="M8 1L2 6l6 5" stroke="#333" stroke-width="2" fill="none"/></svg></div>
<div class="abs hero-arrow" style="left:1134px"><svg width="10" height="12"><path d="M2 1l6 5-6 5" stroke="#333" stroke-width="2" fill="none"/></svg></div>

<div class="abs about-photo" role="img" aria-label="Hands holding a smartphone above a keyboard with a potted plant"></div>
<h2 class="abs section-title" style="left:606px;top:652px">Who we are</h2>
<p class="abs about-text" style="top:702px">Sed ut perspiciatis unde omnis iste natus error sit voluptatem accusantium doloremque laudantium, totam rem aperiam, eaque ipsa quae ab illo inventore veritatis et quasi tecto beatae vitae dicta sunt explicabo. Nemo enim ipsam voluptatem quia voluptas sit tur aut odit aut fugit, sed quia consequuntur magni dolores eos qui ratione ...</p>
<p class="abs about-text" style="top:822px">Neque porro quisquam est, qui dolorem ipsum quia dolor sit amet, consectetur, adipisci aliquam quaerat voluptatem. Ut enim ad minima veniam, quis nostrum exercitationem ullam corporis suscipit laboriosam...</p>
<div class="abs btn btn-orange" style="left:606px;top:921px;width:194px;height:50px">Click read more info!</div>

<h2 class="abs section-title center-title" style="top:1069px">What we offer</h2>
<p class="abs center-sub" style="top:1112px">Sed ut perspiciatis unde omnis iste natus error sit voluptatem accusantium doloremque laudantium, totam rem aperiam, eaque ipsa quae ab illo inventore veritatis et quasi architecto beatae vitae dicta sunt explicabo</p>
<div class="abs phones" role="img" aria-label="Two smartphones showing app icon grids"></div>
<div class="abs timeline"></div>
<div class="abs feature-icon" style="top:1205px;background:var(--orange)"><svg width="24" height="24"><circle cx="12" cy="12" r="7" fill="#fff"/></svg></div>
<div class="abs feature-icon" style="top:1338px;background:var(--blue)"><svg width="24" height="24"><circle cx="12" cy="12" r="9" fill="none" stroke="#fff" stroke-width="3"/></svg></div>
<div class="abs feature-icon" style="top:1475px;background:var(--blue)"><svg width="24" height="24"><rect x="3" y="3" width="18" height="18" fill="#fff"/></svg></div>
<h3 class="abs feature-title" style="top:1212px;color:var(--orange)">Perspiciatis unde omnis iste</h3>
<p class="abs feature-text" style="top:1238px">Sed ut perspiciatis unde omnis iste natus error sit voluptatem antium tempor incididunt ut labore et dolore magna aliqua...</p>
<div class="abs feature-rule" style="top:1312px"></div>
<h3 class="abs feature-title" style="top:1346px;color:var(--blue)">Enim ipsam voluptatem quia</h3>
<p class="abs feature-text" style="top:1372px">Sed ut perspiciatis unde omnis iste natus error sit voluptatem antium tempor incididunt ut labore et dolore magna aliqua...</p>
<div class="abs feature-rule" style="top:1446px"></div>
<h3 class="abs feature-title" style="top:1480px;color:var(--blue)">Accusantium doloremque laudan</h3>
<p class="abs feature-text" style="top:1506px">Sed ut perspiciatis unde omnis iste natus error sit voluptatem antium tempor incididunt ut labore et dolore magna aliqua...</p>
<div class="abs btn btn-orange" style="left:601px;top:1622px;width:202px;height:50px">Start your free trial</div>
<div class="abs btn btn-blue" style="left:812px;top:1622px;width:141px;height:50px;font-size:11px">Click view more info</div>

<section class="abs pricing" role="img" aria-label="Blurred evening city lights background"></section>
<h2 class="abs section-title center-title" style="top:1804px;color:var(--white)">Pricing</h2>
<p class="abs center-sub" style="top:1848px;color:#e6e6e6">Sed ut perspiciatis unde omnis iste natus error sit voluptatem accusantium doloremque laudantium, totam rem aperiam, eaque ipsa quae ab illo inventore veritatis et quasi architecto beatae vitae dicta sunt explicabo</p>

<div class="abs price-card" style="left:243px;top:1935px;width:234px;height:344px">
  <div class="plan">NIMBUS APP</div><div class="amount">$299.00</div><div class="per">Per month</div>
  <ul class="plan-list"><li>Omnis iste natus error sit totam</li><li>Voluptas sit aspernatur</li><li>Omnis iste natus error sit totam</li><li>Voluptas sit aspernatur</li></ul>
  <div class="btn btn-blue card-btn">Get started ›</div>
</div>
<div class="abs price-card featured" style="left:477px;top:1928px;width:246px;height:367px">
  <div class="plan">HTML5 APP</div><div class="amount">$199.00</div><div class="per">Per month</div>
  <ul class="plan-list"><li>Omnis iste natus error sit totam</li><li>Voluptas sit aspernatur</li><li>Omnis iste natus error sit totam</li><li>Voluptas sit aspernatur</li></ul>
  <div class="btn btn-orange card-btn">Get started ›</div>
</div>
<div class="abs price-card" style="left:723px;top:1935px;width:234px;height:344px">
  <div class="plan">ORBIT APP</div><div class="amount">$189.00</div><div class="per">Per month</div>
  <ul class="plan-list"><li>Omnis iste natus error sit totam</li><li>Voluptas sit aspernatur</li><li>Omnis iste natus error sit totam</li><li>Voluptas sit aspernatur</li></ul>
  <div class="btn btn-blue card-btn">Get started ›</div>
</div>

<section class="abs testimonials"></section>
<h2 class="abs section-title center-title" style="top:2417px">Testimonials</h2>
<svg class="abs" style="left:396px;top:2542px" width="12" height="16"><path d="M9 2L3 8l6 6" stroke="#aaa" stroke-width="2" fill="none"/></svg>
<svg class="abs" style="left:792px;top:2542px" width="12" height="16"><path d="M3 2l6 6-6 6" stroke="#aaa" stroke-width="2" fill="none"/></svg>
<div class="abs quote-disc">“</div>
<div class="abs avatar" role="img" aria-label="Portrait of the client giving the testimonial"></div>
<span class="abs quote-mark" style="left:118px;top:2612px">“</span>
<p class="abs quote-text">Sed ut perspiciatis unde omnis iste natus error sit voluptatem accusantium doloremque laudantium, totam rem aperiam, eaque ipsa quae ab illo inventore veritatis et quasi architecto beatae vitae dicta sunt explicabo. Nemo enim ipsam voluptatem quia voluptas sit aspernatur aut odit aut fugit, sed quia consequuntur magni dolores eos qui ratione voluptatem sequi nesciunt.Neque porro quisquam est, qui dolorem ipsum quia dolor sit amet.</p>
<span class="abs quote-mark" style="left:870px;top:2700px">”</span>
<p class="abs author"><b>John Doe</b> (App developer)</p>

<section class="abs contact" role="img" aria-label="Smiling woman looking at her smartphone outdoors"></section>
<h2 class="abs heading" style="left:100px;top:2881px;font-size:26px;font-weight:500;color:var(--white)">QUICK CONTACT FORM</h2>
<div class="abs field" style="left:100px;top:2944px;width:280px;height:52px">First Name</div>
<div class="abs field" style="left:386px;top:2944px;width:280px;height:52px">Last Name</div>
<div class="abs field" style="left:100px;top:3006px;width:280px;height:52px">Email Address</div>
<div class="abs field" style="left:386px;top:3006px;width:280px;height:52px">Phone Number</div>
<div class="abs field" style="left:100px;top:3068px;width:566px;height:100px">Message</div>
<div class="abs btn btn-orange" style="left:104px;top:3184px;width:232px;height:42px;border:4px solid rgba(255,255,255,.35)">Click here to subscription</div>

<footer class="abs site-footer"></footer>
<p class="abs foot-links" style="color:var(--white)">Home &nbsp;/&nbsp; Who we are &nbsp;/&nbsp; What we offer &nbsp;/&nbsp; Pricing &nbsp;/&nbsp; Testimonials &nbsp;/&nbsp; Contact</p>
<p class="abs foot-copy" style="color:var(--white)">Copyrights©Ventra 2016 | Allrights reserved</p>
<p class="abs" style="left:810px;top:3340px;font-size:10px;color:var(--white);text-transform:uppercase;white-space:nowrap">Follow with us :</p>
<div class="abs social" style="left:910px;top:3325px"></div>
<div class="abs social" style="left:956px;top:3325px"></div>
<div class="abs social" style="left:1002px;top:3325px"></div>
<div class="abs social" style="left:1048px;top:3318px;width:54px;height:54px;display:flex;align-items:center;justify-content:center"><svg width="16" height="16"><path d="M8 14V3M3 8l5-5 5 5" stroke="#fff" stroke-width="2" fill="none"/></svg></div>

</body>
</html>
```